Updated web design for software design firm supporting entrepreneurs

Looking for a more modern looking, mobile friendly website design for our company, Plans4Buildables. P4B is a software development firm who supports people who have ideas for software and want to make them a reality. It also provides some maintenance work on existing websites as well as mobile apps. Please see our current website, www.plans4buildables-example.com, for more information on our business.

Old logo files included for reference. However, we are hoping to incorporate a new logo.

Like a blue'ish theme, but open to ideas.

Industry/Entity Type

Software

Logo Text

P4B and/or Plans4Buildables

Number of Pages Required

2 page

Font styles to use
Serif
Sans Serif

Colors
33a6d7
0255a3

Requirements
Must have
• Looking for 2 pages designed: 1 landing page and 1 type of secondary content page
• Please prepare menu for about 7 pages
Nice to have
• This will be implemented as a WordPress theme.
• Could include post-it note, white board, napkins, etc.

```html
<!DOCTYPE html>
<html lang="en">
<head>
<meta charset="utf-8">
<title>Plans4Buildables – Turning your Software Vision into Reality</title>
<link href="https://fonts.googleapis.com/css2?family=Roboto+Condensed:wght@300;400;700&family=Roboto:wght@300;400;500&family=Lato:wght@400;700&display=swap" rel="stylesheet">
<style>
:root{
  --brand-light:#33a6d7;
  --brand-dark:#0255a3;
  --ink:#1a1a1a;
  --muted:#6b6b6b;
  --panel-grey:#f2f2f2;
  --footer-dark:#2a2a2a;
  --footer-mid:#343434;
  --footer-base:#262626;
  --white:#ffffff;
  --tile-label:rgba(2,85,163,.82);
}
*{margin:0;padding:0;box-sizing:border-box}
html,body{width:1200px;height:2344px;overflow:hidden;background:var(--white)}
body{position:relative;font-family:"Roboto",Arial,sans-serif;color:var(--ink)}
.abs{position:absolute}

/* header */
.site-header{position:absolute;left:0;top:0;width:1200px;height:70px}
.brand{position:absolute;left:78px;top:20px;display:flex;align-items:center;gap:12px}
.brand-dot{width:30px;height:30px;border-radius:50%;background:var(--brand-dark)}
.brand-name{font-family:"Roboto",sans-serif;font-size:22px;color:var(--brand-light);letter-spacing:.5px;text-transform:uppercase}
.main-nav{position:absolute;right:81px;top:27px;display:flex;gap:25px;font-family:"Roboto Condensed",sans-serif;font-size:14px;text-transform:uppercase}
.main-nav a{color:#8a8a8a;text-decoration:none}
.main-nav a.is-current{color:#333}

/* hero */
.hero-mark{position:absolute;left:0;width:1200px;top:190px;text-align:center;font-family:"Roboto Condensed",sans-serif;font-weight:700;font-size:120px;color:#8f9193;line-height:1}
.hero-title{position:absolute;left:0;width:1200px;top:382px;text-align:center;font-family:"Roboto",sans-serif;font-size:62px;color:var(--brand-light);line-height:1;text-transform:uppercase}
.hero-tagline{position:absolute;left:0;width:1200px;top:455px;text-align:center;font-family:"Roboto Condensed",sans-serif;font-size:52px;color:var(--ink);line-height:1}
.btn{display:flex;align-items:center;justify-content:center;background:var(--brand-dark);color:var(--white);font-family:"Lato",sans-serif;text-transform:uppercase;text-decoration:none}
.hero-cta{position:absolute;left:527px;top:552px;width:146px;height:53px;font-size:16px}

/* about + how */
.about{position:absolute;left:0;top:677px;width:600px;height:678px;background:var(--brand-light);color:var(--white)}
.how{position:absolute;left:600px;top:677px;width:600px;height:678px;background:var(--panel-grey)}
.section-title{font-family:"Roboto Condensed",sans-serif;font-size:41px;line-height:1;text-transform:uppercase}
.about .section-title{position:absolute;left:80px;top:55px}
.section-sub{position:absolute;font-size:16px}
.about .section-sub{left:80px;top:100px}
.about-photo{position:absolute;left:78px;top:146px;width:447px;height:166px;background:linear-gradient(100deg,#2c3238 0%,#4a5560 55%,#8b96a0 100%)}
.about-copy{position:absolute;left:80px;width:460px;font-size:14.5px;line-height:24px}
.about-cta{position:absolute;left:78px;top:573px;width:208px;height:52px;font-size:14px;font-weight:700}
.how .section-title{position:absolute;left:55px;top:55px;color:var(--brand-dark)}
.how .section-sub{left:55px;top:100px;color:#555}
.step{position:absolute;left:55px;width:440px}
.step-icon{width:50px;height:50px}
.step-rule{width:70px;height:1px;background:#b9b9b9;margin:4px 0 12px}
.step-title{font-family:"Roboto",sans-serif;font-size:21px;color:var(--ink);text-transform:uppercase;line-height:1}
.step-text{font-size:14px;color:#555;line-height:21px;margin-top:6px}

/* portfolio */
.portfolio-title{position:absolute;left:0;width:1200px;top:1407px;text-align:center;color:var(--brand-dark)}
.tile{position:absolute;width:250px;height:248px;overflow:hidden}
.tile-label{position:absolute;left:0;bottom:0;width:100%;height:52px;background:var(--tile-label);color:var(--white);font-family:"Roboto Condensed",sans-serif;font-size:23px;line-height:52px;padding-left:24px}
.tile-feature{position:absolute;left:342px;top:1730px;width:516px;height:248px;background:var(--brand-dark);color:var(--white);text-align:center}
.tile-feature .feature-name{position:absolute;left:0;width:100%;top:72px;font-family:"Roboto Condensed",sans-serif;font-size:26px}
.tile-feature .feature-go{position:absolute;left:233px;top:125px;width:50px;height:50px;border-radius:50%;background:var(--white)}

/* footer */
.footer-brand{position:absolute;left:0;top:2031px;width:290px;height:250px;background:var(--footer-dark);display:flex;align-items:center;justify-content:center}
.footer-brand span{font-family:"Roboto Condensed",sans-serif;font-weight:700;font-size:56px;color:#8f9193}
.footer-main{position:absolute;left:290px;top:2031px;width:582px;height:250px;background:var(--footer-mid);color:var(--white)}
.footer-head{position:absolute;top:30px;font-family:"Roboto Condensed",sans-serif;font-size:19px;text-transform:uppercase}
.footer-list{position:absolute;list-style:none;font-size:14px}
.social-list{left:46px;top:74px;text-transform:uppercase;font-size:13.5px}
.social-list li{height:36px;color:#6d6d6d}
.social-list li:first-child{color:var(--white)}
.link-list{left:201px;top:68px}
.link-list li{height:31px;color:#d8d8d8}
.link-list li::before{content:"›";margin-right:10px;color:var(--white)}
.contact-row{position:absolute;left:330px;display:flex;gap:16px;font-size:14px;line-height:24px;color:var(--white)}
.contact-row svg{flex:none;margin-top:4px}
.odd-jobs{position:absolute;left:872px;top:2031px;width:328px;height:250px;background:var(--brand-light);color:var(--white);text-align:center}
.odd-jobs h3{position:absolute;left:0;width:100%;top:40px;font-family:"Roboto Condensed",sans-serif;font-weight:400;font-size:30px}
.odd-jobs p{position:absolute;left:0;width:100%;top:92px;font-size:16px;line-height:24px}
.odd-jobs .btn{position:absolute;left:90px;top:167px;width:146px;height:50px;font-size:14px;font-weight:700}
.legal{position:absolute;left:0;top:2281px;width:1200px;height:63px;background:var(--footer-base);color:var(--white);text-align:center;line-height:63px;font-size:13px;font-weight:500}
</style>
</head>
<body>

<header class="site-header">
  <div class="brand"><span class="brand-dot"></span><span class="brand-name">Plans4Buildables</span></div>
  <nav class="main-nav">
    <a class="is-current" href="#">Home</a><a href="#">About</a><a href="#">How it works?</a><a href="#">Who needs us?</a><a href="#">Odd jobs</a><a href="#">Portfolio</a><a href="#">Contact</a>
  </nav>
</header>

<section class="hero">
  <div class="hero-mark">P4B</div>
  <h1 class="hero-title">Plans4Buildables</h1>
  <p class="hero-tagline">Turning your Software Vision into Reality</p>
  <a class="btn hero-cta" href="#">Get Started</a>
</section>

<section class="about">
  <h2 class="section-title">About Plans4Buildables</h2>
  <p class="section-sub">Welcome to PLANS4BUILDABLES</p>
  <div class="about-photo" role="img" aria-label="Photo of a hand in a suit sketching interlocking gears on a dark board"></div>
  <p class="about-copy" style="top:346px">We understand that you don't have to be a big company to have big ideas, but turning those ideas into functional software can be time consuming, expensive and seem out of reach. Plans4Buildables specializes in helping small businesses and individuals take their idea from the back of a napkin to the desktop.</p>
  <p class="about-copy" style="top:490px">As a small business ourselves, we understand the need to be flexible, efficient and cost-conscious. We'll take your idea from a vision in your head to a fully working system.</p>
  <a class="btn about-cta" href="#">Set Free Consultation</a>
</section>

<section class="how">
  <h2 class="section-title">How it works</h2>
  <p class="section-sub">How do I get a piece of working software?</p>

  <div class="step" style="top:184px">
    <svg class="step-icon" viewBox="0 0 50 50" fill="none" stroke="#33a6d7" stroke-width="2.5">
      <path d="M25 12a10 10 0 0 0-6 18v5h12v-5a10 10 0 0 0-6-18z" fill="#33a6d7"/>
      <path d="M20 39h10M21 43h8"/>
      <path d="M25 2v5M8 9l4 4M42 9l-4 4M3 24h5M42 24h5"/>
    </svg>
    <div class="step-rule"></div>
    <div class="step-title">Idea</div>
    <p class="step-text">First, Come Up with Your Idea.</p>
  </div>

  <div class="step" style="top:332px">
    <svg class="step-icon" viewBox="0 0 50 50" fill="none" stroke="#33a6d7" stroke-width="2.5">
      <path d="M6 8c3-3 6-3 8 0l4 6c1 2 0 4-2 5l-2 2c2 5 6 9 11 11l2-2c1-2 3-3 5-2l3 2" />
      <rect x="22" y="26" width="24" height="17" rx="2"/>
      <path d="M22 28l12 8 12-8"/>
    </svg>
    <div class="step-rule"></div>
    <div class="step-title">Contact us</div>
    <p class="step-text">Next, contact us to set up a consultation (phone, talkwave or in-person if appropriate) to discuss the details.</p>
  </div>

  <div class="step" style="top:496px">
    <svg class="step-icon" viewBox="0 0 50 50" fill="none" stroke="#33a6d7" stroke-width="2.5">
      <circle cx="18" cy="26" r="6"/>
      <path d="M18 12v4M18 36v4M4 26h4M28 26h4M8 16l3 3M25 33l3 3M8 36l3-3M25 19l3-3"/>
      <path d="M30 30l14-20 4 3-14 20-6 2z" fill="#33a6d7"/>
    </svg>
    <div class="step-rule"></div>
    <div class="step-title">Develop</div>
    <p class="step-text">Together, we will fine tune this plan and use it as the basis for a contract to get the job done.</p>
  </div>
</section>

<section class="portfolio">
  <h2 class="section-title portfolio-title">Our Portfolio</h2>

  <div class="tile" style="left:78px;top:1469px;background:linear-gradient(160deg,#dfe8ef,#8fa9bf)" role="img" aria-label="Photo of a hand touching a glowing video play screen">
    <div class="tile-label">Video Projects</div>
  </div>
  <div class="tile" style="left:342px;top:1469px;background:linear-gradient(160deg,#eef0f2,#c9b8a8)" role="img" aria-label="Photo of a hand holding a phone with a health app">
    <div class="tile-label">Mobile Apps</div>
  </div>
  <div class="tile" style="left:608px;top:1469px;background:linear-gradient(160deg,#e4edf3,#9db9cf)" role="img" aria-label="Photo of hands holding a tablet with a glowing globe">
    <div class="tile-label">Online Publishing</div>
  </div>
  <div class="tile" style="left:872px;top:1469px;background:linear-gradient(160deg,#f3f4f5,#c8ccd2)" role="img" aria-label="Photo of a hand with a pen beside a monitor showing charts">
    <div class="tile-label">API Integration</div>
  </div>

  <div class="tile" style="left:78px;top:1730px;background:linear-gradient(160deg,#7c8790,#3c4650)" role="img" aria-label="Photo of a smartphone full of app icons with earphones on a wooden table">
    <div class="tile-label">Social Networking</div>
  </div>
  <div class="tile-feature">
    <div class="feature-name">Mapping Software</div>
    <svg class="feature-go" viewBox="0 0 50 50"><circle cx="25" cy="25" r="25" fill="#fff"/><path d="M19 18l7 7-7 7M26 18l7 7-7 7" fill="none" stroke="#0255a3" stroke-width="2.5"/></svg>
  </div>
  <div class="tile" style="left:872px;top:1730px;background:linear-gradient(160deg,#f4efe8,#c9a77c)" role="img" aria-label="Photo of cardboard boxes in a shopping cart on a laptop">
    <div class="tile-label">E-commerce</div>
  </div>
</section>

<footer>
  <div class="footer-brand"><span>P4B</span></div>
  <div class="footer-main">
    <div class="footer-head" style="left:46px">Follow us</div>
    <ul class="footer-list social-list"><li>Friendbook</li><li>Chirper</li><li>Searchly +</li><li>WorkLinked</li></ul>
    <div class="footer-head" style="left:201px">Links</div>
    <ul class="footer-list link-list"><li>Home</li><li>About Us</li><li>Services</li><li>Demo</li><li>Contact Us</li></ul>
    <div class="footer-head" style="left:330px">Contact info</div>
    <div class="contact-row" style="top:64px">
      <svg width="16" height="20" viewBox="0 0 16 20"><path d="M8 0a7 7 0 0 0-7 7c0 5 7 13 7 13s7-8 7-13a7 7 0 0 0-7-7z" fill="#fff"/><circle cx="8" cy="7" r="2.6" fill="#343434"/></svg>
      <div>PLANS4BUILDABLES<br>Lakeside County, USA.</div>
    </div>
    <div class="contact-row" style="top:114px">
      <svg width="16" height="16" viewBox="0 0 16 16"><path d="M3 1l3 3-2 2c1 2 3 4 5 5l2-2 3 3-2 3C6 15 1 10 0 4z" fill="#fff"/></svg>
      <div>(555) 014-7788</div>
    </div>
    <div class="contact-row" style="top:148px">
      <svg width="16" height="12" viewBox="0 0 16 12"><rect width="16" height="12" fill="#fff"/><path d="M0 0l8 6 8-6" fill="none" stroke="#343434" stroke-width="1.4"/></svg>
      <div>questions@plans4buildables-<br>example.com</div>
    </div>
  </div>
  <div class="odd-jobs">
    <h3>ODD JOBS</h3>
    <p>We enjoy taking on<br>software-related odd jobs.</p>
    <a class="btn" href="#">Contact Us</a>
  </div>
  <div class="legal">© 2016. All Rights Reserved.</div>
</footer>

</body>
</html>
```